Bref créative
Design tri fold brochure for automotive detailing business
Marble Crest Automotive Detailing
We would like all the information from our service menu to be included in our marketing materials. These items can be found on our website www.marblecrestauto.example
Automotive
target audience includes: residential neighborhoods, car dealerships, mechanics, automotive stores and businesses.
use of our logo
website info
phone number
mobile and fixed locations
www.marblecrestauto.example
logo vector file

```html
<!DOCTYPE html>
<html lang="en">
<head>
<meta charset="utf-8">
<title>Marble Crest Automotive Detailing – Tri-fold Brochure</title>
<link href="https://fonts.googleapis.com/css2?family=Oswald:wght@400;600&family=Open+Sans:wght@400;600;700&display=swap" rel="stylesheet">
<style>
:root{
  --page:#e9e7e4;
  --ink-dark:#141518;
  --panel-dark:#1c1e22;
  --navy:#0d2a55;
  --blue:#1d63b8;
  --blue-light:#3f8ae0;
  --rule:#3a3d44;
  --text-light:#c9ccd2;
  --text-dim:#8c919a;
  --text-body:#4a4d52;
  --white:#ffffff;
}
*{box-sizing:border-box;margin:0;padding:0}
html,body{width:1200px;height:589px;overflow:hidden;background:var(--page);font-family:"Open Sans",Arial,sans-serif}
.canvas{position:relative;width:1200px;height:589px}
.sheet{position:absolute;top:34px;width:540px;height:520px;box-shadow:0 4px 14px rgba(0,0,0,.25);overflow:hidden}

/* inside sheet */
.inside{left:32px;background:var(--ink-dark);color:var(--text-light)}
.brand-col{position:absolute;left:0;top:0;width:132px;height:490px;padding:14px 10px;border-right:1px solid var(--rule)}
.brand{display:flex;align-items:center;gap:6px;margin-bottom:16px}
.brand-dot{width:18px;height:18px;border-radius:50%;background:var(--blue);flex:none}
.brand-name{font-family:"Oswald",sans-serif;font-weight:600;font-size:10px;line-height:1.1;color:var(--white);text-transform:uppercase}
.intro{font-size:5.5px;line-height:1.5;color:var(--text-dim);margin-bottom:8px}
.list{list-style:none;font-size:5.5px;line-height:1.75;color:var(--text-light)}
.list li::before{content:"› ";color:var(--blue-light)}
.brand-photo{position:absolute;left:0;bottom:0;width:132px;height:190px;background:radial-gradient(circle at 55% 45%,#5a5e66 0,#2a2c31 45%,#15161a 80%)}
.services-title{position:absolute;left:132px;top:8px;width:408px;text-align:center;font-family:"Oswald",sans-serif;font-size:20px;letter-spacing:6px;color:var(--white)}
.note{position:absolute;right:10px;top:10px;font-size:5px;color:var(--text-dim);line-height:1.4}
.svc{position:absolute;width:204px;padding:0 8px}
.svc-head{height:14px;margin:0 -8px 6px;padding:0 8px;background:linear-gradient(var(--blue-light),var(--blue));font-family:"Oswald",sans-serif;font-size:7px;line-height:14px;color:var(--white);text-transform:uppercase}
.svc-1{left:132px;top:38px}.svc-2{left:336px;top:38px;border-left:1px solid var(--rule)}
.svc-3{left:132px;top:232px}.svc-4{left:336px;top:232px;border-left:1px solid var(--rule)}
.price{float:right;color:var(--blue-light)}
.footer-band{position:absolute;left:0;bottom:0;width:540px;height:30px;background:linear-gradient(var(--blue-light),var(--navy));display:flex;justify-content:space-around;align-items:center;font-family:"Oswald",sans-serif;font-size:9px;letter-spacing:.5px;color:var(--white);text-transform:uppercase}

/* outside sheet */
.outside{left:628px;background:var(--white)}
.panel{position:absolute;top:0;height:520px}
.why{left:0;width:180px;padding:16px 14px;color:var(--text-body)}
.why h2{font-size:8px;font-weight:700;color:var(--ink-dark);margin-bottom:6px}
.why h3{font-size:5.5px;font-weight:700;color:var(--ink-dark);margin:6px 0 2px}
.why p{font-size:5.3px;line-height:1.55}
.cover{left:180px;width:170px}
.cover-band{position:absolute;left:40px;top:0;width:34px;height:240px;background:linear-gradient(var(--navy),var(--blue))}
.cover-logo{position:absolute;left:22px;top:318px;display:flex;align-items:center;gap:7px}
.cover-logo .brand-dot{width:24px;height:24px}
.cover-logo .brand-name{color:var(--navy);font-size:11px}
.cover-contact{position:absolute;left:0;bottom:40px;width:170px;text-align:center;font-size:5.5px;line-height:1.6;color:var(--text-body)}
.cover-contact b{color:var(--ink-dark)}
.back{left:350px;width:190px;background:var(--panel-dark);color:var(--text-light)}
.back-band{position:absolute;left:0;top:0;width:190px;height:70px;background:linear-gradient(90deg,var(--navy),var(--blue))}
.back-web{position:absolute;top:120px;width:190px;text-align:center;font-size:6.5px;color:var(--white)}
.back-info{position:absolute;left:24px;top:176px;font-size:5.5px;line-height:1.6;color:var(--text-light);text-transform:uppercase}
.back-photo{position:absolute;left:0;bottom:0;width:190px;height:230px;background:radial-gradient(circle at 60% 55%,#9aa0a8 0,#4b4f57 38%,#1c1e22 78%)}
</style>
</head>
<body>
<main class="canvas">

  <section class="sheet inside" aria-label="Brochure inside spread">
    <div class="brand-col">
      <div class="brand"><span class="brand-dot"></span><span class="brand-name">Marble Crest<br>Automotive Detailing</span></div>
      <p class="intro">Mobile and fixed location detailing for homes, dealerships, garages and fleets.</p>
      <ul class="list">
        <li>Hand Wash &amp; Dry</li><li>Clay Bar Treatment</li><li>Machine Polish</li><li>Carnauba Wax</li>
        <li>Paint Sealant</li><li>Tire &amp; Trim Dressing</li><li>Wheel Cleaning</li><li>Glass Treatment</li>
        <li>Engine Bay Detail</li><li>Headlight Restore</li><li>Odor Removal</li><li>Fleet Plans</li>
      </ul>
      <div class="brand-photo" role="img" aria-label="Photo of a car steering wheel and dashboard"></div>
    </div>

    <h1 class="services-title">SERVICES</h1>
    <p class="note">* Prices vary by vehicle size<br>* Mobile service available</p>

    <div class="svc svc-1">
      <div class="svc-head">Full Detail · Interior &amp; Exterior</div>
      <ul class="list">
        <li>Hand Wash &amp; Dry<span class="price">$189</span></li><li>Clay Bar Decontamination</li><li>One Step Polish</li>
        <li>Wax or Sealant</li><li>Wheels &amp; Tires Cleaned</li><li>Full Vacuum</li><li>Seats Shampooed</li>
        <li>Leather Conditioned</li><li>Dash &amp; Panels Dressed</li><li>Windows In &amp; Out</li><li>Door Jambs Wiped</li>
        <li>Carpet Extraction</li><li>Air Freshener</li>
      </ul>
    </div>
    <div class="svc svc-2">
      <div class="svc-head">Express · Interior &amp; Exterior</div>
      <ul class="list">
        <li>Hand Wash<span class="price">$79</span></li><li>Spray Wax</li><li>Tire Shine</li><li>Wheels Cleaned</li>
        <li>Quick Vacuum</li><li>Dash Wipe Down</li><li>Windows Cleaned</li><li>Mats Cleaned</li>
        <li>Door Jambs Wiped</li><li>Trim Dressed</li>
      </ul>
    </div>
    <div class="svc svc-3">
      <div class="svc-head">Exterior Only</div>
      <ul class="list">
        <li>Hand Wash &amp; Dry<span class="price">$99</span></li><li>Clay Bar Treatment</li><li>Machine Polish</li>
        <li>Paint Sealant</li><li>Trim Restoration</li><li>Wheel Wells Cleaned</li><li>Bug &amp; Tar Removal</li>
        <li>Headlight Restoration</li><li>Paint Touch-Up</li><li>Engine Bay Detail</li>
      </ul>
    </div>
    <div class="svc svc-4">
      <div class="svc-head">Interior Only</div>
      <ul class="list">
        <li>Full Vacuum<span class="price">$109</span></li><li>Seat Shampoo</li><li>Carpet Extraction</li>
        <li>Leather Clean &amp; Condition</li><li>Headliner Spot Clean</li><li>Vents &amp; Console</li>
        <li>Odor Removal</li><li>Pet Hair Removal</li><li>Glass Cleaned</li>
      </ul>
    </div>

    <div class="footer-band">
      <span>Auto Detailing</span><span>Headlight Restoration</span><span>Odor Removal</span><span>Paint Touch-Up</span><span>Wheel Repair</span>
    </div>
  </section>

  <section class="sheet outside" aria-label="Brochure outside spread">
    <div class="panel why">
      <h2>Why Us?</h2>
      <p>Marble Crest brings years of detailing care to every car, truck and fleet we touch. We use quality products and careful hands to protect your finish.</p>
      <h3>We come to you</h3>
      <p>Our mobile unit serves homes, offices and dealer lots, or visit our fixed bay for a full shop detail.</p>
      <h3>Trusted by local businesses</h3>
      <p>Dealerships, mechanics and auto stores rely on us for lot prep, trade-ins and showroom ready vehicles.</p>
      <h3>Fair, clear pricing</h3>
      <p>Every service is priced up front by vehicle size, with no hidden fees and no surprise charges.</p>
      <h3>Satisfaction guaranteed</h3>
      <p>If something is missed, tell us and we will return to make it right at no extra cost.</p>
    </div>

    <div class="panel cover">
      <div class="cover-band"></div>
      <div class="cover-logo"><span class="brand-dot"></span><span class="brand-name">Marble Crest<br>Automotive Detailing</span></div>
      <p class="cover-contact"><b>FERNCLIFF HARBOR, ST 00000</b><br>Telephone (555) 014-2290<br>hello@marblecrestauto.example</p>
    </div>

    <div class="panel back">
      <div class="back-band"></div>
      <p class="back-web">www.marblecrestauto.example</p>
      <p class="back-info">418 Harbor Line Rd<br>Ferncliff Harbor, ST 00000<br>Mobile &amp; fixed locations<br>Open Mon – Sat<br>Call (555) 014-2290</p>
      <div class="back-photo" role="img" aria-label="Photo of a polished car wheel and tire"></div>
    </div>
  </section>

</main>
</body>
</html>
```